Retail Appliance Store Chain needs NEW business Card

Name of my company is Brandon's Appliances brandonsappliances.com is our website. . We are a 2 location brick and mortar, and online store selling premium, luxury, and normal household appliances, such as ovens, stoves, cooktops, dishwashers, refrigerators, washers and dryers, grills, air conditioners etc. The focus is on large kitchen appliances and laundry appliances.
Please visit http://brandonsappliances.com to get a feel for the business and branding.
I have attached the Brandon's Appliances logo (i do not have eps or psd or ai). And I have also attached our current business cards that we use. We have two versions. A double sided version for managers, and a one side version for regular employees.
Please submit BOTH one sided and two sided designs if possible.
Please keep consistent with the Brandon's Appliances logo, colors, etc.
I would prefer no rounded corners on the business card designs for printing costs.
Information on the cards (in no particular order):
Name - Employee Name
Business name - Brandon's Appliances
website - brandonsappliances.com
Email - Employee Email
2 Phone Numbers - store 1 address, store 2 address
2 Addresses - store 1 address, store 2 address

*do NOT need Fax #

Industry/Entity Type

Home Appliance

Contact Information for Business Card

Logo - Brandons Appliances Logo
Name - Employee Name
Email - Employee Email

Please no rounded corners. Standard US Business Card Size please.

Font styles to use
Serif
Sans Serif

Requirements
Must have
• colors and design that somewhat match the feel of current logo and website
Should not have
• No rounded corners.
No non-traditional business card size. US Standard Business Card Size only

```html
<!DOCTYPE html>
<html lang="en">
<head>
<meta charset="utf-8">
<title>Brandon's Appliances – Business Card</title>
<link href="https://fonts.googleapis.com/css2?family=Montserrat:wght@300;400;600;700&display=swap" rel="stylesheet">
<style>
  :root {
    --brand-blue: #24508f;
    --card-white: #f7f7f8;
    --card-shade: #e9eaec;
    --backdrop: #3b3c3e;
    --ink-light: #ffffff;
    --subtitle: #c9d6ea;
  }
  * { box-sizing: border-box; margin: 0; padding: 0; }
  html, body { width: 1200px; height: 1000px; overflow: hidden; }
  body {
    background: var(--backdrop);
    font-family: "Montserrat", Arial, sans-serif;
    display: flex; align-items: center; justify-content: center;
  }
  .business-card {
    position: relative;
    width: 1000px; height: 572px;
    border-radius: 0;
    overflow: hidden;
    background: var(--card-white);
  }
  .card-texture {
    position: absolute; inset: 0;
    background: linear-gradient(135deg, var(--card-white) 0%, var(--card-shade) 45%, var(--card-white) 70%, var(--card-shade) 100%);
  }
  .brand-name {
    position: absolute; left: 90px; top: 110px;
    font-size: 64px; font-weight: 700; color: var(--brand-blue);
    letter-spacing: 0.5px; white-space: nowrap;
  }
  .info-band {
    position: absolute; left: 0; right: 0; top: 230px; height: 200px;
    background: var(--brand-blue);
  }
  .employee {
    position: absolute; left: 90px; top: 40px; color: var(--ink-light);
    white-space: nowrap;
  }
  .employee-name { font-size: 46px; font-weight: 700; letter-spacing: 0.5px; line-height: 1.15; }
  .employee-title { font-size: 20px; font-weight: 300; color: var(--subtitle); margin-top: 6px; }
  .employee-email { font-size: 27px; font-weight: 600; margin-top: 8px; }
  .band-divider {
    position: absolute; left: 590px; top: 36px; width: 2px; height: 128px;
    background: rgba(255,255,255,0.7);
  }
  .contact-list {
    position: absolute; left: 628px; top: 40px; list-style: none; color: var(--ink-light);
  }
  .contact-item { display: flex; align-items: center; height: 60px; white-space: nowrap; }
  .contact-item svg { width: 26px; height: 26px; margin-right: 24px; flex-shrink: 0; }
  .contact-phone { font-size: 26px; font-weight: 600; }
  .contact-web { font-size: 19px; font-weight: 600; }
  .store-addresses {
    position: absolute; left: 90px; top: 452px; list-style: none;
    color: var(--brand-blue); font-weight: 700; font-size: 30px; line-height: 48px;
    white-space: nowrap;
  }
</style>
</head>
<body>
  <article class="business-card">
    <div class="card-texture" role="img" aria-label="Faint light grey low-poly background texture"></div>

    <div class="brand-name">Brandon's Appliances</div>

    <section class="info-band">
      <div class="employee">
        <div class="employee-name">EVAN MARSH</div>
        <div class="employee-title">Bargain Basement Supervisor</div>
        <div class="employee-email">evanm@brandonsappliances.com</div>
      </div>

      <div class="band-divider"></div>

      <ul class="contact-list">
        <li class="contact-item">
          <svg viewBox="0 0 26 26" aria-hidden="true">
            <path d="M3 9c0-3 4-5 10-5s10 2 10 5v2h-5V9c-2-1-8-1-10 0v2H3z" fill="#fff"/>
            <path d="M7 12h12l3 9H4z" fill="#fff"/>
            <circle cx="13" cy="16.5" r="2.5" fill="#24508f"/>
          </svg>
          <span class="contact-phone">(860) 555-0142</span>
        </li>
        <li class="contact-item">
          <svg viewBox="0 0 26 26" aria-hidden="true">
            <path d="M3 9c0-3 4-5 10-5s10 2 10 5v2h-5V9c-2-1-8-1-10 0v2H3z" fill="#fff"/>
            <path d="M7 12h12l3 9H4z" fill="#fff"/>
            <circle cx="13" cy="16.5" r="2.5" fill="#24508f"/>
          </svg>
          <span class="contact-phone">(860) 555-0178</span>
        </li>
      </ul>
    </section>

    <ul class="store-addresses">
      <li class="store-address">145 Harbor Mill Rd. Easton, CT 06612</li>
      <li class="store-address">88 Quarry Hill Ave. Easton, CT 06612</li>
    </ul>
  </article>
</body>
</html>
```